New Webpage for High Class Expert Witness Services Company

We are looking for a minimalist design for a webpage that just has our logo and an entry form offer to connect with one of our Liaisons.
The entry form should just ask for Name, Email, Contact Info and Description of Project.

Company Name is: The Marlow Crest Advisory Services

Number of Pages Required

1 page

```html
<!DOCTYPE html>
<html lang="en">
<head>
<meta charset="utf-8">
<title>The Marlow Crest Advisory Services — Connect with Our Liaisons</title>
<link rel="stylesheet" href="https://fonts.googleapis.com/css2?family=Montserrat:wght@400;500;600&display=swap">
<style>
  :root {
    --page-bg: #f4f4f4;
    --page-bg-light: #fdfdfd;
    --band-line: #e2e2e2;
    --ink-dark: #3a3a3a;
    --card-bg: #1b1b1b;
    --field-bg: #242424;
    --field-text: #a3a3a3;
    --title-text: #ffffff;
    --subtitle-text: #a8a8a8;
    --accent-grey: #999999;
    --button-text: #111111;
    --footer-text: #555555;
  }
  * { box-sizing: border-box; margin: 0; padding: 0; }
  html, body { width: 1200px; height: 663px; overflow: hidden; }
  body {
    position: relative;
    font-family: "Montserrat", Arial, sans-serif;
    background: radial-gradient(ellipse at 50% 45%, var(--page-bg-light) 0%, var(--page-bg) 70%, #ececec 100%);
  }
  .backdrop { position: absolute; inset: 0; width: 1200px; height: 663px; }
  .brand {
    position: absolute; top: 62px; left: 0; width: 1200px;
    display: flex; justify-content: center; align-items: center; gap: 12px;
  }
  .brand-mark { width: 30px; height: 30px; background: var(--ink-dark); }
  .brand-name {
    font-weight: 500; font-size: 20px; letter-spacing: 0.06em;
    color: var(--ink-dark); text-transform: uppercase; line-height: 1.15;
  }
  .contact-card {
    position: absolute; left: 284px; top: 177px; width: 632px; height: 398px;
    background: var(--card-bg); border-radius: 8px;
    box-shadow: 0 10px 40px rgba(0,0,0,0.22);
  }
  .card-bar {
    position: absolute; left: 29px; top: 0; width: 575px; height: 6px;
    background: var(--accent-grey); border-radius: 0 0 4px 4px;
  }
  .card-title {
    position: absolute; left: 33px; top: 28px;
    font-size: 17px; font-weight: 500; color: var(--title-text);
  }
  .card-subtitle {
    position: absolute; left: 33px; top: 57px;
    font-size: 11.5px; color: var(--subtitle-text);
  }
  .contact-form { position: absolute; left: 32px; top: 92px; width: 569px; }
  .field {
    display: block; width: 100%; height: 35px; margin-bottom: 9px;
    background: var(--field-bg); border: none; border-radius: 3px;
    padding: 0 14px; font-family: inherit; font-size: 10px; color: var(--field-text);
  }
  .field::placeholder { color: var(--field-text); }
  .field-description { height: 95px; padding-top: 12px; resize: none; }
  .submit-button {
    display: block; width: 100%; height: 35px; margin-top: 1px;
    background: var(--accent-grey); border: none; border-radius: 3px;
    font-family: inherit; font-weight: 600; font-size: 9.5px;
    letter-spacing: 0.04em; color: var(--button-text);
  }
  .site-footer {
    position: absolute; top: 620px; left: 0; width: 1200px; text-align: center;
    font-size: 8px; letter-spacing: 0.04em; color: var(--footer-text);
  }
</style>
</head>
<body>
  <svg class="backdrop" viewBox="0 0 1200 663" aria-hidden="true">
    <g fill="none" stroke="var(--band-line)" stroke-width="1.2">
      <line x1="0" y1="318" x2="300" y2="440"/>
      <line x1="0" y1="478" x2="420" y2="663"/>
      <line x1="0" y1="550" x2="260" y2="663"/>
      <line x1="760" y1="0" x2="1200" y2="190"/>
      <line x1="900" y1="0" x2="1200" y2="120"/>
      <line x1="880" y1="210" x2="1200" y2="340"/>
    </g>
    <polygon points="0,320 300,442 300,663 0,663" fill="#ffffff" opacity="0.35"/>
    <polygon points="900,0 1200,0 1200,120" fill="#ffffff" opacity="0.5"/>
  </svg>

  <header class="brand">
    <span class="brand-mark"></span>
    <span class="brand-name">The Marlow Crest<br>Advisory Services</span>
  </header>

  <main class="contact-card">
    <div class="card-bar"></div>
    <h1 class="card-title">Connect with Our Liaisons</h1>
    <p class="card-subtitle">Please fill out the form below.</p>
    <form class="contact-form">
      <input class="field" type="text" placeholder="Your Name">
      <input class="field" type="email" placeholder="Your Email">
      <input class="field" type="tel" placeholder="Your Phone Number">
      <textarea class="field field-description" placeholder="Description of Project"></textarea>
      <button class="submit-button" type="button">SUBMIT</button>
    </form>
  </main>

  <footer class="site-footer">COPYRIGHT © 2026 MARLOW CREST ADVISORY SERVICES. ALL RIGHTS RESERVED.</footer>
</body>
</html>
```